Voltara Solutions Ltd - Project for new electric vehicle charging company

Please use Voltara Solutions Ltd logo & artwork instead of Brightwell.

We would like to produce a leaflet to advertise our electric vehicle charging company to build a reputation and workflow in the local area.

We would like to use the attached logo and maintain the colour palette of the of the logo to be simple, modern and effective.

I have over 15 years experience in the electrical industry and have direct access to the latest technology in electric vehicle charging.

All quotes to remain fixed costs subject to survey of the property and maintenance options can be available.

We can also offer further remedial works to any property through our sister company Brightwell Solutions Ltd.

Target Market(s)

Domestic / commercial customers

Requirements
Must have
• Voltara Solutions Ltd logo and colour palette.
Should not have
• Brightwell logo, Email or website address.

```html
<!DOCTYPE html>
<html lang="en">
<head>
<meta charset="utf-8">
<title>Fully Charged – Voltara Solutions Ltd Leaflet</title>
<link href="https://fonts.googleapis.com/css2?family=Poppins:wght@200;400;800&display=swap" rel="stylesheet">
<style>
  :root{
    --teal:#1fb29c;
    --grey-text:#8d8d8d;
    --ink:#1e1e1e;
    --band-grey:#e2e2e2;
    --paper:#ffffff;
    --backdrop:#ececec;
    --photo-1:#cfdde6;
    --photo-2:#e6eef3;
  }
  *{margin:0;padding:0;box-sizing:border-box}
  html,body{width:1200px;height:960px;overflow:hidden}
  body{background:var(--backdrop);font-family:"Poppins",sans-serif;position:relative}
  .leaflet{position:absolute;left:282px;top:30px;width:636px;height:900px;background:var(--paper);overflow:hidden;box-shadow:0 4px 18px rgba(0,0,0,.12)}
  .hero-photo{position:absolute;left:0;top:40px;width:636px;height:520px;
    background:
      linear-gradient(to bottom,rgba(255,255,255,0) 55%,var(--paper) 100%),
      linear-gradient(120deg,#9fb3c2 0%,var(--photo-1) 30%,var(--photo-2) 60%,#f4f7f9 100%);}
  .shapes{position:absolute;inset:0}
  .brand{position:absolute;right:36px;top:38px;display:flex;align-items:center;gap:12px;color:var(--paper);font-weight:400;font-size:24px;letter-spacing:.3px;white-space:nowrap}
  .brand-dot{width:34px;height:34px;border-radius:50%;background:var(--paper);flex:none}
  .headline{position:absolute;left:88px;top:512px;color:var(--teal);line-height:1}
  .headline .light{display:block;font-weight:200;font-size:52px;letter-spacing:1px}
  .headline .bold{display:block;font-weight:800;font-size:62px;margin-top:2px}
  .tagline{position:absolute;left:90px;top:642px;color:var(--grey-text);font-size:20px;font-weight:400;white-space:nowrap}
  .body-copy{position:absolute;left:90px;top:684px;width:450px;color:var(--ink);font-size:14.5px;line-height:22px;font-weight:400}
  .contacts{position:absolute;left:90px;top:824px;list-style:none;font-family:Arial,Helvetica,sans-serif;font-size:12px;color:var(--ink)}
  .contacts li{display:flex;align-items:center;gap:7px;height:15px;white-space:nowrap}
  .contacts svg{width:11px;height:11px;flex:none}
  .address{position:absolute;right:36px;top:824px;color:var(--teal);font-family:Arial,Helvetica,sans-serif;font-size:11.5px;white-space:nowrap}
</style>
</head>
<body>
<main class="leaflet">
  <div class="hero-photo" role="img" aria-label="Photograph of a white electric car plugged into a charging point with a glowing blue ring"></div>

  <svg class="shapes" viewBox="0 0 636 900" width="636" height="900" aria-hidden="true">
    <polygon class="header-band" points="230,0 636,0 636,92 292,132" fill="var(--teal)"/>
    <circle cx="520" cy="470" r="78" fill="#ffffff" style="filter:drop-shadow(0 3px 5px rgba(0,0,0,.25))"/>
    <circle cx="520" cy="470" r="66" fill="var(--teal)"/>
    <g fill="#ffffff" stroke="#ffffff">
      <rect x="468" y="448" width="24" height="42" rx="2" stroke="none"/>
      <rect x="463" y="488" width="34" height="5" rx="1" stroke="none"/>
      <rect x="472" y="453" width="16" height="10" fill="var(--teal)" stroke="none"/>
      <polygon points="481,468 475,479 480,479 477,487 485,475 480,475" fill="var(--teal)" stroke="none"/>
      <path d="M492 460 h6 v22 q0 8 8 8 h8" fill="none" stroke-width="2.5"/>
      <path d="M516 476 l8 -12 h32 l8 12 h4 v14 h-6 v5 h-8 v-5 h-28 v5 h-8 v-5 h-6 v-14 z" stroke="none"/>
      <path d="M527 474 l5 -7 h22 l5 7 z" fill="var(--teal)" stroke="none"/>
      <circle cx="524" cy="482" r="3" fill="var(--teal)" stroke="none"/>
      <circle cx="562" cy="482" r="3" fill="var(--teal)" stroke="none"/>
    </g>
    <polygon class="footer-grey" points="0,815 330,815 375,872 0,872" fill="var(--band-grey)"/>
    <polygon class="footer-stripe" points="330,815 372,815 420,872 378,872" fill="var(--teal)"/>
    <rect x="0" y="872" width="420" height="14" fill="var(--teal)"/>
    <line x1="372" y1="816" x2="600" y2="816" stroke="var(--teal)" stroke-width="3"/>
  </svg>

  <div class="brand"><span class="brand-dot"></span>Voltara Solutions Ltd</div>

  <h1 class="headline"><span class="light">FULLY</span><span class="bold">CHARGED!</span></h1>
  <p class="tagline">The Electric Vehicle Charging</p>
  <p class="body-copy">Lorem ipsum dolor sit amet, consectetuer adipiscing elit, sed diam nonummy nibh euismod tincidunt ut laoreet dolore magna aliquam erat volutpat. Ut wisi enim ad minim veniam, quis nostrud exerci tation ullamcorper suscipit lobortis nisl ut aliquip ex ea commodo consequat.</p>

  <ul class="contacts">
    <li><svg viewBox="0 0 12 12"><circle cx="6" cy="6" r="6" fill="var(--teal)"/><path d="M4 3 l1.2 1.6 -0.7 0.8 q0.8 1.6 2.1 2.1 l0.8 -0.7 1.6 1.2 -0.8 1 q-3.6 -0.6 -5.2 -5 z" fill="#fff"/></svg>0121-496-0187</li>
    <li><svg viewBox="0 0 12 12"><circle cx="6" cy="6" r="6" fill="var(--teal)"/><rect x="3" y="4" width="6" height="4.2" fill="#fff"/><path d="M3 4 l3 2.4 3 -2.4" fill="none" stroke="var(--teal)" stroke-width=".8"/></svg>enquiries@voltara.com</li>
    <li><svg viewBox="0 0 12 12"><circle cx="6" cy="6" r="6" fill="var(--teal)"/><circle cx="6" cy="6" r="3" fill="none" stroke="#fff" stroke-width="1"/><line x1="3" y1="6" x2="9" y2="6" stroke="#fff" stroke-width=".8"/></svg>www.voltara-solutions.co.uk</li>
  </ul>
  <p class="address">12 Faraday House, Coventry, CV1 2ZZ</p>
</main>
</body>
</html>
```